Business Card Design Project

I want a new business card for all 5 of my companies. Card needs to be double sided with my name and details on one side and all 5 logos on the other side.

Industry/Entity Type

Business

```html
<!DOCTYPE html>
<html lang="en">
<head>
<meta charset="utf-8">
<title>Business Card Concepts</title>
<link rel="stylesheet" href="https://fonts.googleapis.com/css2?family=Arimo:wght@400;700&display=swap">
<style>
  :root {
    --stage-dark: #000005;
    --stage-glow: #0b0d22;
    --card-bg: #0b0b0c;
    --card-edge: #5a5a5e;
    --line: #c9c9cc;
    --text-light: #ffffff;
    --text-muted: #b9bcc4;
    --mascot-yellow: #f2c200;
    --mascot-red: #d8261c;
    --mascot-blue: #1f6fd0;
    --seal-blue: #7fb4ea;
    --struct-green: #9cc83a;
  }
  * { box-sizing: border-box; margin: 0; padding: 0; }
  html, body { width: 1200px; height: 900px; overflow: hidden; }
  body {
    background: radial-gradient(ellipse at 50% 50%, var(--stage-glow) 0%, var(--stage-dark) 75%);
    font-family: "Arimo", Arial, sans-serif;
    position: relative;
  }
  .card {
    position: absolute;
    width: 428px; height: 275px;
    background: var(--card-bg);
    border: 1px solid var(--card-edge);
    overflow: hidden;
  }
  .card--spread { left: 188px; top: 173px; }
  .card--row-high { left: 638px; top: 173px; }
  .card--row-low { left: 194px; top: 478px; }
  .card--banner { left: 638px; top: 478px; }
  .card__lines { position: absolute; inset: 0; }
  .card__lines path { fill: none; stroke: var(--line); stroke-width: 0.9; }
  .mascot {
    position: absolute;
    border-radius: 6px;
    background: linear-gradient(160deg, var(--mascot-yellow) 0%, var(--mascot-red) 55%, var(--mascot-blue) 100%);
    opacity: 0.9;
  }
  .mascot-name {
    position: absolute;
    transform: translateX(-50%);
    white-space: nowrap;
    color: var(--text-light);
    font-weight: 700;
    letter-spacing: -0.3px;
  }
  .brand {
    position: absolute;
    display: flex;
    align-items: center;
    gap: 3px;
  }
  .brand__dot { border-radius: 50%; flex: none; }
  .brand__dot--seal { background: var(--seal-blue); }
  .brand__dot--struct { background: var(--struct-green); }
  .brand__name {
    color: var(--text-muted);
    font-weight: 400;
    line-height: 1.05;
  }
  .group-line {
    position: absolute;
    transform: translateX(-50%);
    white-space: nowrap;
    color: var(--text-muted);
  }
  .size-lg .mascot-name { font-size: 11px; }
  .size-sm .mascot-name { font-size: 7.5px; }
  .size-sm .brand__name, .size-lg .brand__name { font-size: 7px; }
  .size-sm .brand__dot, .size-lg .brand__dot { width: 9px; height: 9px; }
  .size-sm .group-line, .size-lg .group-line { font-size: 7.5px; }
  .card--banner .mascot-name { font-size: 8px; }
  .card--banner .brand__name { font-size: 7.5px; }
  .card--banner .brand__dot { width: 11px; height: 11px; }
  .card--banner .group-line { font-size: 10px; }
</style>
</head>
<body>

<!-- Concept 1: staggered mascots -->
<section class="card card--spread size-lg">
  <svg class="card__lines" width="428" height="275" viewBox="0 0 428 275">
    <path d="M20 23 H123 L303 163 H401"/>
    <path d="M20 83 L199 221"/>
    <path d="M3 211 L20 223 H129"/>
    <path d="M248 240 H401 L428 213"/>
  </svg>
  <div class="mascot" style="left:101px;top:62px;width:58px;height:64px" role="img" aria-label="Cartoon builder mascot holding a wrench beside scaffolding"></div>
  <span class="mascot-name" style="left:133px;top:128px">Mr. Frame</span>
  <div class="mascot" style="left:318px;top:80px;width:70px;height:64px" role="img" aria-label="Cartoon builder mascot beside a temporary fence panel"></div>
  <span class="mascot-name" style="left:357px;top:148px">Mr. Barrier</span>
  <div class="mascot" style="left:28px;top:140px;width:68px;height:64px" role="img" aria-label="Cartoon builder mascot running with a trowel"></div>
  <span class="mascot-name" style="left:60px;top:208px">Mr. Mend</span>
  <div class="brand" style="left:284px;top:208px"><span class="brand__dot brand__dot--seal"></span><span class="brand__name">Civic Sealant<br>Services</span></div>
  <div class="brand" style="left:353px;top:201px"><span class="brand__dot brand__dot--struct"></span><span class="brand__name">Varenna<br>Structural</span></div>
  <span class="group-line" style="left:340px;top:239px">A Varenna Group Company</span>
</section>

<!-- Concept 2: mascot row, upper -->
<section class="card card--row-high size-sm">
  <svg class="card__lines" width="428" height="275" viewBox="0 0 428 275">
    <path d="M2 145 L29 170 H245"/>
    <path d="M235 240 H404 L428 213"/>
  </svg>
  <div class="mascot" style="left:44px;top:113px;width:38px;height:42px" role="img" aria-label="Cartoon builder mascot with a trowel"></div>
  <span class="mascot-name" style="left:63px;top:157px">Mr. Mend</span>
  <div class="mascot" style="left:104px;top:113px;width:40px;height:42px" role="img" aria-label="Cartoon builder mascot with a wrench and scaffolding"></div>
  <span class="mascot-name" style="left:125px;top:157px">Mr. Frame</span>
  <div class="mascot" style="left:161px;top:113px;width:46px;height:42px" role="img" aria-label="Cartoon builder mascot beside a fence panel"></div>
  <span class="mascot-name" style="left:185px;top:157px">Mr. Barrier</span>
  <div class="brand" style="left:286px;top:208px"><span class="brand__dot brand__dot--seal"></span><span class="brand__name">Civic Sealant<br>Services</span></div>
  <div class="brand" style="left:354px;top:200px"><span class="brand__dot brand__dot--struct"></span><span class="brand__name">Varenna<br>Structural</span></div>
  <span class="group-line" style="left:340px;top:244px">A Varenna Group Company</span>
</section>

<!-- Concept 3: mascot row, lower -->
<section class="card card--row-low size-sm">
  <svg class="card__lines" width="428" height="275" viewBox="0 0 428 275">
    <path d="M2 113 L35 138 H275"/>
    <path d="M13 187 H400 L428 160"/>
  </svg>
  <div class="mascot" style="left:40px;top:82px;width:42px;height:40px" role="img" aria-label="Cartoon builder mascot with a trowel"></div>
  <span class="mascot-name" style="left:63px;top:124px">Mr. Mend</span>
  <div class="mascot" style="left:102px;top:82px;width:42px;height:40px" role="img" aria-label="Cartoon builder mascot with a wrench and scaffolding"></div>
  <span class="mascot-name" style="left:123px;top:124px">Mr. Frame</span>
  <div class="mascot" style="left:160px;top:82px;width:48px;height:40px" role="img" aria-label="Cartoon builder mascot beside a fence panel"></div>
  <span class="mascot-name" style="left:186px;top:124px">Mr. Barrier</span>
  <div class="brand" style="left:284px;top:155px"><span class="brand__dot brand__dot--seal"></span><span class="brand__name">Civic Sealant<br>Services</span></div>
  <div class="brand" style="left:353px;top:148px"><span class="brand__dot brand__dot--struct"></span><span class="brand__name">Varenna<br>Structural</span></div>
  <span class="group-line" style="left:339px;top:192px">A Varenna Group Company</span>
</section>

<!-- Concept 4: centred banner -->
<section class="card card--banner">
  <svg class="card__lines" width="428" height="275" viewBox="0 0 428 275">
    <path d="M0 128 L33 155 L0 182"/>
    <path d="M428 128 L395 155 L428 182"/>
    <path d="M33 155 H395"/>
  </svg>
  <div class="mascot" style="left:44px;top:96px;width:42px;height:40px" role="img" aria-label="Cartoon builder mascot with a trowel"></div>
  <span class="mascot-name" style="left:64px;top:138px">Mr. Mend</span>
  <div class="mascot" style="left:111px;top:96px;width:42px;height:40px" role="img" aria-label="Cartoon builder mascot with a wrench and scaffolding"></div>
  <span class="mascot-name" style="left:132px;top:138px">Mr. Frame</span>
  <div class="mascot" style="left:182px;top:96px;width:48px;height:40px" role="img" aria-label="Cartoon builder mascot beside a fence panel"></div>
  <span class="mascot-name" style="left:207px;top:138px">Mr. Barrier</span>
  <div class="brand" style="left:255px;top:116px"><span class="brand__dot brand__dot--seal"></span><span class="brand__name">Civic Sealant<br>Services</span></div>
  <div class="brand" style="left:340px;top:109px"><span class="brand__dot brand__dot--struct"></span><span class="brand__name">Varenna<br>Structural</span></div>
  <span class="group-line" style="left:198px;top:162px">A Varenna Group Company</span>
</section>

</body>
</html>
```